Career development coaching - school lever to adults, needs a business card

Tandem Lark - An independent Career Advice business that provides 1-2-1 advice,for career development, entrepreneurial support and workshops needs a business card. Our clients of all ages (school leaver to adults looking for a career move) and universities and colleges. We would like the card to be double-sided with a modern, professional look. Looking for something professional yet very creative and original. Want a standard size business card that inspires a second look because it stands out from the rest.

One side of the card to have a design incorporating the logo with Tandem Lark name with the strap line “Helping you find your future” and space for the company website

Other side of the card to the logo/Tandem Lark name and the usual contact information:
Individual Name
Job Title (for example, Director)
Phone number
Email address
Company website address

Facebook, LinkedIn and Twitter links will need to go somewhere (back or front!)

The design will be used for 3 individuals so should be editable so that we can update as needed/as we grow.

Attached is the company logo/colours to be incorporated.

Target Market(s)

1-2-1 advice,for career development, entrepreneurial support and workshops needs a business card. Our clients of all ages (school leaver to adults looking for a career move) and universities and colleges.

Industry/Entity Type

Consulting

Contact Information for Business Card

Individual Name
Phone number
Email address
Company website address

Font styles to use
Sans Serif

Colors
0255a3
3176b5
faa54b
f78f20
85acd3
cfdeed

Requirements
Must have
• use the Tandem Lark Logo in some way - using the colours and the blue/orange palette
• For the logo - hope this makes sense to someone or if they direclty relate to the logo image attached!
• For the Orange:- Pantone 1585 C
• In CMYK : C3 M71 Y100 K0
• For the Blue:- 100% Pantone 7469 C
• In CMYK : C100 M62 Y27 K7
• Please feel free to contact me with any questions for more info
Nice to have
• happy to see any creative designs
Should not have
• Nothing too traditional,

```html
<!DOCTYPE html>
<html lang="en">
<head>
<meta charset="utf-8">
<title>Tandem Lark – Business Card</title>
<link href="https://fonts.googleapis.com/css2?family=Dosis:wght@600&family=Roboto:wght@400&display=swap" rel="stylesheet">
<style>
  :root {
    --page-bg: #ebebeb;
    --card-top: #242424;
    --card-bottom: #040404;
    --brand-blue: #0e5a7e;
    --brand-orange: #e8793a;
    --text-light: #f2f2f2;
  }
  * { box-sizing: border-box; margin: 0; padding: 0; }
  html, body {
    width: 1200px; height: 443px; overflow: hidden;
    background: var(--page-bg);
  }
  .canvas { position: relative; width: 1200px; height: 443px; }
  .card {
    position: absolute; top: 73px;
    width: 484px; height: 292px;
    border-radius: 14px;
    background: linear-gradient(180deg, var(--card-top) 0%, var(--card-bottom) 100%);
    overflow: hidden;
  }
  .card--front { left: 82px; }
  .card--back { left: 602px; width: 480px; }

  /* Front */
  .front-mark {
    position: absolute; left: 50%; top: 88px;
    width: 70px; height: 70px; margin-left: -35px;
    border-radius: 50%; background: var(--brand-blue);
  }
  .front-name {
    position: absolute; left: 0; right: 0; top: 178px;
    text-align: center;
    font-family: "Dosis", sans-serif; font-weight: 600;
    font-size: 30px; letter-spacing: 1px;
    color: var(--brand-orange);
  }

  /* Back */
  .back-brand {
    position: absolute; left: 36px; top: 108px; width: 180px;
    text-align: center;
    font-family: "Dosis", sans-serif; font-weight: 600;
    font-size: 30px; color: var(--brand-orange);
  }
  .person { position: absolute; left: 245px; top: 74px; }
  .person-name {
    font-family: "Dosis", sans-serif; font-weight: 600;
    font-size: 22px; line-height: 1; color: var(--brand-orange);
  }
  .person-title {
    margin-top: 6px;
    font-family: "Roboto", sans-serif; font-size: 12.5px;
    color: var(--text-light);
  }
  .contact-list {
    position: absolute; left: 245px; top: 130px; list-style: none;
    font-family: "Roboto", sans-serif; font-size: 13.5px; color: var(--text-light);
  }
  .contact-list li { display: flex; align-items: center; height: 17.5px; }
  .contact-icon { width: 12px; height: 12px; margin-right: 11px; fill: var(--brand-orange); }

  .footer-band { position: absolute; left: 0; bottom: 0; width: 480px; height: 40px; }
  .social {
    position: absolute; left: 288px; bottom: 9px;
    display: flex; align-items: center;
    font-family: "Roboto", sans-serif; font-size: 15px; color: var(--text-light);
  }
  .social-mark {
    width: 11px; height: 11px; margin-right: 8px;
    background: var(--text-light); border-radius: 2px;
  }
</style>
</head>
<body>
<main class="canvas">
  <section class="card card--front" aria-label="Card front">
    <div class="front-mark"></div>
    <div class="front-name">Tandem Lark</div>
  </section>

  <section class="card card--back" aria-label="Card back">
    <div class="back-brand">Tandem Lark</div>

    <div class="person">
      <div class="person-name">Your Good Name</div>
      <div class="person-title">Managing Director</div>
    </div>

    <ul class="contact-list">
      <li>
        <svg class="contact-icon" viewBox="0 0 12 12" aria-hidden="true">
          <path d="M1 3c0-1.2 1-2 2.5-2h5C10 1 11 1.8 11 3v1H8.5V3h-5v1H1z"/>
          <path d="M2 5h8l1 6H1z M4.5 6.5a1.5 1.5 0 1 0 3 0a1.5 1.5 0 1 0 -3 0" fill-rule="evenodd"/>
        </svg>
        +00 111 22 33 44
      </li>
      <li>
        <svg class="contact-icon" viewBox="0 0 12 12" aria-hidden="true">
          <path fill-rule="evenodd" d="M6 0.5a5.5 5.5 0 1 1 0 11a5.5 5.5 0 1 1 0-11z M6 1.6c-0.6 0.6-1.2 2-1.3 3.7h2.6C7.2 3.6 6.6 2.2 6 1.6z M1.7 5.3h2c0.1-1.4 0.5-2.6 1-3.4a4.4 4.4 0 0 0-3 3.4z M7.3 1.9c0.5 0.8 0.9 2 1 3.4h2a4.4 4.4 0 0 0-3-3.4z M1.7 6.7a4.4 4.4 0 0 0 3 3.4c-0.5-0.8-0.9-2-1-3.4z M4.7 6.7c0.1 1.7 0.7 3.1 1.3 3.7c0.6-0.6 1.2-2 1.3-3.7z M8.3 6.7c-0.1 1.4-0.5 2.6-1 3.4a4.4 4.4 0 0 0 3-3.4z"/>
        </svg>
        www.yourwebsite.com
      </li>
      <li>
        <svg class="contact-icon" viewBox="0 0 12 12" aria-hidden="true">
          <path d="M0.5 2.5h11v7h-11z M1.5 3.2l4.5 3.5l4.5-3.5" fill-rule="evenodd"/>
          <path d="M1 3l5 4l5-4" fill="none" stroke="#111" stroke-width="0.9"/>
        </svg>
        yourname@yourwebsite.com
      </li>
    </ul>

    <svg class="footer-band" viewBox="0 0 480 40" aria-hidden="true">
      <rect x="0" y="28" width="240" height="12" fill="var(--brand-orange)"/>
      <polygon points="232,0 480,0 480,40 200,40" fill="var(--brand-blue)"/>
    </svg>
    <div class="social">
      <span class="social-mark"></span>/tandemlark
    </div>
  </section>
</main>
</body>
</html>
```